Presence Leadership Model

I am looking for a graphic design of the attached leadership model. The colors and design can be altered in any manner that brings the model alive version of the house model.

```html
<!DOCTYPE html>
<html lang="en">
<head>
<meta charset="utf-8">
<title>Presence Leadership Model</title>
<link rel="stylesheet" href="https://fonts.googleapis.com/css2?family=Oswald:wght@500;700&family=Montserrat:wght@700;800&family=Open+Sans:wght@400;700&display=swap">
<style>
:root{
  --ink:#1b1b1b;
  --blue:#0a1fd0;
  --yellow:#fcc800;
  --yellow-dark:#7a5f00;
  --cyan:#55ffff;
  --cyan-dark:#0c7f9c;
  --green:#1ad300;
  --green-dark:#0d4f00;
  --red:#ff3d0a;
  --red-dark:#8a0f00;
  --text:#1e1e1e;
}
*{margin:0;padding:0;box-sizing:border-box}
html,body{width:794px;height:1200px;overflow:hidden;background:#fff}
.poster{position:relative;width:794px;height:1200px;overflow:hidden;font-family:"Open Sans",Arial,sans-serif;color:var(--text)}
.spine{position:absolute;left:0;top:0;width:134px;height:1166px;background:var(--ink)}
.col{position:absolute;top:0;height:1166px}
.col-org{left:134px;width:221px;background:linear-gradient(90deg,#c4ffff,#fff)}
.col-inter{left:355px;width:222px;background:linear-gradient(90deg,#c6ffbd,#fff)}
.col-personal{left:577px;width:217px;background:linear-gradient(90deg,#ffcccc,#fff)}
.col-inter::before,.col-personal::before{content:"";position:absolute;left:0;top:370px;width:6px;height:796px;background:linear-gradient(90deg,rgba(0,0,0,.28),rgba(0,0,0,0))}
.map{position:absolute;left:290px;top:30px;width:504px;height:270px;border-radius:40% 30% 45% 35%;background:radial-gradient(ellipse at 55% 45%,rgba(160,160,160,.28),rgba(160,160,160,0) 70%)}
.title{position:absolute;left:161px;top:166px;font-family:"Oswald",sans-serif;font-weight:700;font-size:46px;letter-spacing:17px;color:var(--blue);line-height:1}
.tagline{position:absolute;left:161px;top:234px;font-family:"Montserrat",sans-serif;font-weight:800;font-size:20.5px;line-height:27px;color:#222}
.banner{position:absolute;left:85px;width:632px;height:64px;background:var(--yellow);border-top-right-radius:48px;box-shadow:2px 3px 4px rgba(0,0,0,.2)}
.banner-outer{top:305px}
.banner-inner{top:952px}
.banner h2{position:absolute;top:14px;font-family:"Montserrat",sans-serif;font-weight:700;font-size:28.5px;letter-spacing:1.5px;color:#1a1a1a;white-space:nowrap}
.banner-outer h2{left:83px}
.banner-inner h2{left:78px}
.banner svg{position:absolute;left:18px;top:10px}
.fold{position:absolute;width:49px;height:24px}
.fold-yellow{background:linear-gradient(90deg,var(--yellow-dark),var(--yellow))}
.fold-cyan{background:linear-gradient(90deg,var(--cyan-dark),#10a8c8)}
.fold-green{background:linear-gradient(90deg,var(--green-dark),#062800)}
.fold-red{background:linear-gradient(90deg,var(--red-dark),#2a0000)}
.fold{clip-path:polygon(0 0,100% 0,100% 100%)}
.icon{position:absolute;top:392px;width:60px;height:60px}
.tab{position:absolute;top:462px;width:189px;height:64px;border-top-right-radius:40px;box-shadow:2px 3px 4px rgba(0,0,0,.18)}
.tab span{position:absolute;left:13px;top:7px;font-family:"Oswald",sans-serif;font-weight:500;font-size:24px;line-height:25px;color:#fff;letter-spacing:.2px}
.tab-org{left:85px;background:var(--cyan)}
.tab-inter{left:306px;background:var(--green)}
.tab-personal{left:528px;background:var(--red)}
.heading{position:absolute;top:541px;font-weight:700;font-size:16.5px;white-space:nowrap}
.heading-org{left:146px;color:var(--blue)}
.heading-inter{left:368px;color:var(--green)}
.heading-personal{left:595px;color:var(--red)}
.list{position:absolute;list-style:none;font-size:16.5px;line-height:30.5px}
.list li{position:relative;padding-left:29px}
.list li::before{content:"";position:absolute;left:2px;top:13px;width:6px;height:6px;border-radius:50%}
.list-org li::before{background:var(--blue)}
.list-inter li::before{background:var(--green)}
.list-personal li::before{background:var(--red)}
.list li .cont{display:block;padding-left:2px}
.list-org{left:146px;top:562px}
.list-inter{left:368px;top:562px}
.list-personal{left:595px;top:563px;line-height:24px}
.list-personal li::before{top:10px}
.list-personal .cont{margin-top:6px}
.inner-org{left:146px;top:1048px;line-height:24px}
.inner-inter{left:368px;top:1048px}
.inner-personal{left:595px;top:1046px;line-height:24px}
.inner-org li::before,.inner-personal li::before{top:10px}
.arrow{position:absolute;top:646px;width:40px;height:40px}
</style>
</head>
<body>
<main class="poster">
  <div class="spine"></div>
  <div class="col col-org"></div>
  <div class="col col-inter"></div>
  <div class="col col-personal"></div>
  <div class="map" role="img" aria-label="Faint world map in the background"></div>

  <h1 class="title">PRESENCE</h1>
  <p class="tagline">FOSTER CONTAGIOUS SUCCESS THROUGH PEOPLE,<br>RELATIONSHIPS AND A SHARED VISION</p>

  <section class="banner banner-outer">
    <svg width="46" height="46" viewBox="0 0 46 46" aria-hidden="true" fill="#111" stroke="#111">
      <rect x="1" y="1" width="8" height="7" stroke="none"/>
      <line x1="5" y1="4" x2="5" y2="14" stroke-width="2"/>
      <circle cx="8" cy="16" r="5" stroke="none"/>
      <path d="M34 3l6 6M40 3l-6 6M15 28l6 6M21 28l-6 6" stroke-width="2.2"/>
      <path d="M28 16h-6l3-3M22 16l3 3M28 16q8 0 8 10v8" fill="none" stroke-width="2.2"/>
      <circle cx="36" cy="38" r="6" stroke="none"/>
    </svg>
    <h2>OUTER (IMPACT) STRATEGIES</h2>
  </section>
  <div class="fold fold-yellow" style="left:85px;top:369px"></div>

  <div class="icon" style="left:145px" role="img" aria-label="Team icon"><svg width="60" height="60" viewBox="0 0 60 60"><circle cx="12" cy="8" r="6"/><circle cx="46" cy="8" r="6"/><circle cx="29" cy="35" r="6"/><path d="M1 26a11 9 0 0 1 22 0zM35 26a11 9 0 0 1 22 0zM18 55a11 11 0 0 1 22 0z"/><path d="M8 32q6 18 16 22M50 32q-6 18-16 22M22 13q7-5 14 0" fill="none" stroke="#000" stroke-width="2.5"/></svg></div>
  <div class="icon" style="left:372px" role="img" aria-label="Collaboration icon"><svg width="62" height="60" viewBox="0 0 62 60"><circle cx="31" cy="19" r="16"/><circle cx="31" cy="19" r="7" fill="#fff"/><circle cx="13" cy="43" r="6"/><circle cx="49" cy="43" r="6"/><path d="M2 60a11 10 0 0 1 22 0zM38 60a11 10 0 0 1 22 0z"/></svg></div>
  <div class="icon" style="left:593px" role="img" aria-label="Achievement icon"><svg width="60" height="60" viewBox="0 0 60 60"><path d="M9 2v10q0 10 11 12M41 2v10q0 10-11 12" fill="none" stroke="#000" stroke-width="5"/><circle cx="25" cy="12" r="7"/><circle cx="25" cy="42" r="16"/><path d="M25 31l3.5 7 7.5 1-5.5 5 1.5 7.5-7-4-7 4 1.5-7.5-5.5-5 7.5-1z" fill="none" stroke="#fff" stroke-width="2"/><path d="M2 42h5M43 42h5M5 32l4 2M45 32l-4 2M5 52l4-2M45 52l-4-2" stroke="#000" stroke-width="2"/></svg></div>

  <div class="tab tab-org"><span>ORGANIZATION<br>LEVEL</span></div>
  <div class="fold fold-cyan" style="left:85px;top:526px"></div>
  <div class="tab tab-inter"><span>INTERPERSONAL<br>LEVEL</span></div>
  <div class="fold fold-green" style="left:306px;top:526px"></div>
  <div class="tab tab-personal"><span>PERSONAL<br>LEVEL</span></div>
  <div class="fold fold-red" style="left:528px;top:526px"></div>

  <h3 class="heading heading-org">WINS THEORY</h3>
  <ul class="list list-org">
    <li>Develop concrete<span class="cont">outcomes, and</span><span class="cont">visible results</span></li>
    <li>Foster in-depth<span class="cont">changes, and new</span><span class="cont">practices</span></li>
    <li>Have a micro,<span class="cont">interpersonal or</span><span class="cont">local impact</span></li>
    <li>Cultivate positive<span class="cont">judgement, and</span><span class="cont">shared ambition</span></li>
  </ul>

  <h3 class="heading heading-inter">HEART LISTENING</h3>
  <ul class="list list-inter">
    <li>Ask open-ended<span class="cont">questions</span></li>
    <li>Affirm someone’s<span class="cont">strengths, efforts</span><span class="cont">and past success</span></li>
    <li>Reflect back what<span class="cont">is shared for</span><span class="cont">confirmation</span></li>
    <li>Summarize key<span class="cont">points to gain</span><span class="cont">insights</span></li>
    <li>Share and develop<span class="cont">mutual expertise</span></li>
  </ul>

  <h3 class="heading heading-personal">INSIGHT DIALOGUE</h3>
  <ul class="list list-personal">
    <li>Pause</li>
    <li>Relax</li>
    <li>Open</li>
    <li>Attune to<span class="cont">Emergence</span></li>
    <li>Listen Deeply</li>
    <li>Speak the Truth</li>
  </ul>

  <svg class="arrow" style="left:333px" viewBox="0 0 40 40" aria-hidden="true"><circle cx="20" cy="20" r="19" fill="#3a3a3a" stroke="#fff" stroke-width="1.5"/><path d="M8 20l10-10v6h13v8H18v6z" fill="#fff"/></svg>
  <svg class="arrow" style="left:556px" viewBox="0 0 40 40" aria-hidden="true"><circle cx="20" cy="20" r="19" fill="#3a3a3a" stroke="#fff" stroke-width="1.5"/><path d="M8 20l10-10v6h13v8H18v6z" fill="#fff"/></svg>

  <section class="banner banner-inner">
    <svg width="46" height="46" viewBox="0 0 46 46" aria-hidden="true" fill="#111" stroke="#111">
      <rect x="35" y="1" width="8" height="7" stroke="none"/>
      <line x1="39" y1="4" x2="39" y2="14" stroke-width="2"/>
      <circle cx="36" cy="16" r="5" stroke="none"/>
      <path d="M4 3l6 6M10 3l-6 6M23 28l6 6M29 28l-6 6" stroke-width="2.2"/>
      <path d="M16 16h6l-3-3M22 16l-3 3M16 16q-8 0-8 10v8" fill="none" stroke-width="2.2"/>
      <circle cx="8" cy="38" r="6" stroke="none"/>
    </svg>
    <h2>INNER (WELLBEING) STRATEGIES</h2>
  </section>
  <div class="fold fold-yellow" style="left:85px;top:1016px"></div>

  <ul class="list list-org inner-org">
    <li>Physical Fitness</li>
    <li>Nutrition</li>
  </ul>
  <ul class="list list-inter inner-inter">
    <li>Heart Rate<span class="cont">Variability</span></li>
    <li>Neurofeedback</li>
  </ul>
  <ul class="list list-personal inner-personal">
    <li>Island Hoppin Club</li>
    <li>Video Gaming Club</li>
  </ul>
</main>
</body>
</html>
```